website redesign - bronwickhomes.com.au

need to redesign our website. we are proud of our current website but market feedback suggests that we have to tone down our quirkiness and make it look more professional to target the million dollar market.
right now we appeal to the younger generation so we have to meet somewhere in the middle.
we want to still retain our same flavour and style but need to also look a bit more professional. we need to evolve our brand to a more grown up look.
examples of standard websites include tallow estates, gant dwellings, lodger ledger, fennimore upward, dowsett

```html
<!DOCTYPE html>
<html lang="en">
<head>
<meta charset="utf-8">
<title>Bronwick Homes</title>
<link href="https://fonts.googleapis.com/css2?family=Roboto:wght@300;400;500;700;900&display=swap" rel="stylesheet">
<style>
:root{
  --orange:#ef5a24;
  --orange-soft:#f4a27f;
  --ink:#222226;
  --text:#555;
  --muted:#888;
  --line:#e3e3e3;
  --dark:#1f1f22;
  --purple:#5a2a8c;
  --blue:#2f8fc4;
  --graphite:#4a4a4a;
  --gold:#c89b3c;
  --white:#fff;
}
*{box-sizing:border-box;margin:0;padding:0}
html,body{width:1200px;height:5316px;overflow:hidden}
body{font-family:"Roboto",Arial,sans-serif;color:var(--text);background:var(--white);position:relative;font-size:13px;line-height:1.55}
.abs{position:absolute}
.btn{display:inline-block;background:var(--orange);color:var(--white);font-weight:700;font-size:11px;letter-spacing:1px;padding:9px 22px;border-radius:20px;text-transform:uppercase}
.accent{color:var(--orange)}

/* header */
.topbar{left:0;top:0;width:1200px;height:56px;background:var(--white);z-index:3}
.brand{left:100px;top:16px;font-size:22px;font-weight:700;color:var(--orange);letter-spacing:1px}
.contact-top{right:100px;top:12px;display:flex;align-items:center;gap:16px}
.contact-top .call{font-size:10px;color:var(--muted);line-height:1.2}
.contact-top .call b{display:block;font-size:14px;color:var(--ink)}
.dot{width:22px;height:22px;border-radius:50%;background:#444;display:inline-block}
.nav{left:80px;top:56px;width:1040px;height:30px;background:var(--orange);display:flex;justify-content:center;gap:34px;align-items:center;z-index:3}
.nav span{color:var(--white);font-size:11px;font-weight:500}
.hero{left:0;top:0;width:1200px;height:640px;background:linear-gradient(180deg,#3a2a30 0%,#6b3a2c 35%,#2a2326 70%,#141416 100%)}
.hero-title{left:676px;top:236px;color:var(--white);font-size:64px;font-weight:900;line-height:.95;letter-spacing:1px}
.hero-copy{left:678px;top:378px;width:300px;color:#ddd;font-size:11px;line-height:1.5}
.hero-btn{left:678px;top:436px}

/* welcome */
.welcome-img{left:100px;top:716px;width:430px;height:230px;background:linear-gradient(135deg,#c03226,#3a2f6b 55%,#ddd)}
.welcome-inset{left:306px;top:828px;width:222px;height:204px;background:linear-gradient(135deg,#f2efe9,#b58a60);border:4px solid var(--white)}
.welcome-text{left:640px;top:744px;width:440px}
.welcome-text h2{font-size:18px;font-weight:400;color:var(--ink);line-height:1.2}
.welcome-text h2 b{font-size:28px;font-weight:900}
.welcome-text .lead{font-size:12px;font-weight:700;color:var(--ink);margin:8px 0 10px}
.welcome-text p{font-size:11px}
.welcome-text .btn{margin-top:16px}

/* properties */
.sec-head{font-size:32px;font-weight:700;color:var(--ink)}
.props-head{left:100px;top:1176px}
.tabs{right:100px;top:1226px;font-size:11px;color:var(--muted)}
.tabs .on{color:var(--orange)}
.card{position:absolute;background:linear-gradient(160deg,#8aa7c4,#b9a084 55%,#5b4a3a)}
.card .info{position:absolute;left:18px;bottom:18px;color:var(--white);font-size:11px;font-weight:700;text-transform:uppercase;line-height:1.35}
.card .price{color:var(--orange);font-size:20px;font-weight:900}
.card .more{font-size:10px;font-weight:400;text-transform:none}
.card .feats{position:absolute;right:14px;bottom:18px;display:flex;gap:6px}
.feat{width:24px;height:24px;border-radius:50%;background:var(--purple);color:var(--white);font-size:11px;font-weight:700;display:flex;align-items:center;justify-content:center}
.card.small .price{font-size:15px}
.view-all{left:548px;top:1924px}

/* video */
.video{left:100px;top:2052px;width:1000px;height:416px;background:radial-gradient(circle at 50% 45%,#8c47c8,#3d1f74 55%,#1a0e3a)}
.play{left:560px;top:2196px;width:80px;height:80px}
.video-cap{left:100px;top:2300px;width:1000px;text-align:center;color:var(--white)}
.video-cap b{display:block;font-size:24px;font-weight:500}
.video-cap span{font-size:12px}

/* team */
.team-head{left:100px;top:2474px;line-height:1.2}
.team-head small{display:block;font-size:14px;font-weight:400;color:var(--ink)}
.team-head strong{font-size:32px;font-weight:900;color:var(--ink)}
.team-copy{left:100px;top:2548px;width:700px;font-size:11px}
.team-row{left:180px;top:2664px;width:840px;height:296px;display:flex;gap:4px}
.member{flex:1;position:relative;background:linear-gradient(180deg,#fff 0%,#f3eee9 30%,var(--tone) 100%)}
.member::after{content:"";position:absolute;left:0;right:0;bottom:0;height:3px;background:var(--orange)}
.team-btn{left:548px;top:3000px}

/* testimonials */
.testi-head{left:100px;top:3166px;color:var(--ink);line-height:1.15}
.testi-head small{display:block;font-size:16px;margin-bottom:4px}
.testi-head strong{font-size:30px;font-weight:900}
.testi-band{left:0;top:3300px;width:1200px;height:460px;background:linear-gradient(180deg,#e9e1db,#cfc3b8)}
.quote{position:absolute;color:var(--white);padding:40px;font-size:12px;line-height:1.6}
.quote.main{left:310px;top:3380px;width:580px;height:300px;background:var(--orange);text-align:center}
.quote.side{top:3400px;width:330px;height:260px;background:var(--orange-soft)}
.quote .who{margin-top:14px;font-weight:700;font-size:13px}
.qmark{font-size:54px;font-weight:900;line-height:.6;display:block;margin-bottom:8px}
.pager{left:582px;top:3650px;display:flex;gap:6px}
.pager i{width:8px;height:8px;border-radius:50%;background:rgba(255,255,255,.5)}
.pager i.on{background:var(--white)}

/* awards */
.awards-text{left:100px;top:3836px;width:560px}
.awards-text h2{font-size:30px;font-weight:900;color:var(--ink)}
.awards-text .lead{font-size:13px;font-weight:700;color:var(--ink);margin:6px 0 12px}
.awards-text p{font-size:11px;margin-bottom:8px}
.badge{position:absolute;width:88px;height:88px;border-radius:50%;background:var(--blue);box-shadow:inset 0 0 0 6px var(--white),inset 0 0 0 9px rgba(0,0,0,.12)}
.badge.sq{border-radius:10px}
.badge.dark{background:var(--graphite)}
.badge.gold{width:116px;height:116px;background:var(--gold);box-shadow:inset 0 0 0 8px #a67c26}

/* contact */
.contact-curve{left:0;top:4226px}
.contact-text{left:100px;top:4472px;width:440px}
.contact-text h2{font-size:22px;font-weight:900;color:var(--ink)}
.contact-text p{font-size:11px;margin:8px 0 16px}
.form{display:grid;grid-template-columns:1fr 1fr;gap:10px}
.field{height:32px;background:#eee;border:1px solid var(--line);font-size:10px;color:var(--muted);padding:8px 10px}
.field.wide{grid-column:1/3}
.field.msg{height:64px}
.contact-text .btn{margin-top:14px}
.house{left:560px;top:4340px;width:572px;height:420px;background:linear-gradient(180deg,#7fb3e0 0%,#b6d3ec 40%,#c98f63 62%,#8a6a50 100%)}

/* footer */
.footer{left:0;top:4780px;width:1200px;height:420px;background:var(--dark)}
.f-item{position:absolute;top:4850px;display:flex;gap:14px;color:#ccc;font-size:11px;line-height:1.4}
.f-item b{color:var(--white);display:block;font-size:12px}
.f-ic{width:42px;height:42px;flex:none}
.f-col{position:absolute;top:4990px;color:#bbb;font-size:11px}
.f-col h4{color:var(--white);font-size:14px;margin-bottom:12px}
.f-list{display:grid;grid-template-columns:160px 120px;gap:8px 0}
.f-list span::before{content:"› ";color:var(--orange)}
.f-video{left:868px;top:4990px;width:232px;height:150px;background:linear-gradient(135deg,#6a6a78,#2c2c34)}
.copy{left:100px;top:5252px;font-size:11px;color:var(--muted)}
.copy b{color:var(--orange);font-weight:400}
.socials{right:100px;top:5246px;display:flex;gap:8px}
.socials .dot{background:var(--orange)}
</style>
</head>
<body>

<!-- hero -->
<div class="abs hero" role="img" aria-label="Dusk photograph of modern townhouses lit against an evening sky"></div>
<header class="abs topbar">
  <div class="abs brand">BRONWICK HOMES</div>
  <div class="abs contact-top">
    <div class="call">Call us today<b>0400 555 017</b></div>
    <span class="dot"></span><span class="dot"></span><span class="dot"></span>
  </div>
</header>
<nav class="abs nav">
  <span>Home</span><span>About us</span><span>Properties</span><span>Buy with us</span><span>Property Management</span><span>Advice</span><span>Finance</span><span>Our Team</span><span>Reviews</span><span>Contact</span>
</nav>
<h1 class="abs hero-title">BRONWICK<br>HOMES</h1>
<p class="abs hero-copy">We're not your typical real estate agents. We focus on doing things a little differently, bringing energy and care to every move you make with us.</p>
<span class="abs btn hero-btn">Read More</span>
<svg class="abs" style="left:0;top:540px" width="1200" height="120" viewBox="0 0 1200 120" aria-hidden="true">
  <path d="M0 70 Q600 10 1200 40 L1200 120 L0 120Z" fill="#ef5a24"/>
  <path d="M0 92 Q600 34 1200 62 L1200 120 L0 120Z" fill="#fff"/>
</svg>

<!-- welcome -->
<div class="abs welcome-img" role="img" aria-label="Photograph of the agency shopfront"></div>
<div class="abs welcome-inset" role="img" aria-label="Photograph of a bright modern kitchen interior"></div>
<div class="abs welcome-text">
  <h2>Welcome to<br><b>Bronwick Homes</b></h2>
  <p class="lead">or rather, welcome to the best property experience (pun intended) of your life!</p>
  <p>We're not your typical run-of-the-mill residential real estate agents. We focus on selling and managing residential real estate with a twist. Let's face it, the real estate industry can get a bad rap but we hope to change that by giving every client honest advice, genuine care and a smooth journey from start to finish. Come say hello and see how we work.</p>
  <span class="btn">Read More</span>
</div>

<!-- properties -->
<h2 class="abs sec-head props-head"><span class="accent">O</span>ur Properties</h2>
<div class="abs tabs"><span class="on">For Sale</span> &nbsp;|&nbsp; For Rent &nbsp;|&nbsp; Sold</div>

<div class="card" style="left:100px;top:1264px;width:488px;height:330px" role="img" aria-label="Photograph of a two-storey brick home">
  <div class="info">12 Larkspur Drive,<br>Wendale QLD 4190<br><span class="price">Offers Above $549,000</span><br><span class="more">Read More ›</span></div>
  <div class="feats"><span class="feat">4</span><span class="feat">2</span><span class="feat">2</span></div>
</div>
<div class="card" style="left:604px;top:1264px;width:496px;height:330px;background:linear-gradient(160deg,#efeae4,#c9c0b6 60%,#8a7f74)" role="img" aria-label="Photograph of an open plan living room">
  <div class="info">25 Calder Street,<br>Pine Hollow QLD 4102<br><span class="price">$380,000</span><br><span class="more">Read More ›</span></div>
  <div class="feats"><span class="feat">2</span><span class="feat">1</span><span class="feat">1</span></div>
</div>
<div class="card small" style="left:100px;top:1624px;width:322px;height:250px;background:linear-gradient(160deg,#8fb4d6,#9c8a74 60%,#4f4236)" role="img" aria-label="Photograph of a suburban house front">
  <div class="info">130 Marrow Road,<br>Elmcroft QLD 4071<br><span class="price">Offers Above $449,000</span><br><span class="more">Read More ›</span></div>
  <div class="feats"><span class="feat">3</span><span class="feat">1</span><span class="feat">2</span></div>
</div>
<div class="card small" style="left:438px;top:1624px;width:322px;height:250px;background:linear-gradient(160deg,#d9d2ca,#7d6d5e 60%,#3c332b)" role="img" aria-label="Photograph of a unit living area">
  <div class="info">7/40 Kent Street,<br>Pine Hollow QLD 4102<br><span class="price">$374,000</span><br><span class="more">Read More ›</span></div>
  <div class="feats"><span class="feat">2</span><span class="feat">2</span><span class="feat">1</span></div>
</div>
<div class="card small" style="left:776px;top:1624px;width:324px;height:250px;background:linear-gradient(160deg,#f1ede8,#bdb3a8 60%,#6e645a)" role="img" aria-label="Photograph of a modern kitchen">
  <div class="info">5/85 Orme Street,<br>Riverbend QLD 4128<br><span class="price">$328,500</span><br><span class="more">Read More ›</span></div>
  <div class="feats"><span class="feat">2</span><span class="feat">1</span><span class="feat">1</span></div>
</div>
<span class="abs btn view-all">View All</span>

<!-- video -->
<div class="abs video" role="img" aria-label="Video still of a crowd at a lively event under purple lights"></div>
<svg class="abs play" viewBox="0 0 80 80" aria-hidden="true"><circle cx="40" cy="40" r="40" fill="#fff"/><path d="M32 26 L56 40 L32 54Z" fill="#ef5a24"/></svg>
<div class="abs video-cap"><b>Real Estate Made Awesome!</b><span>Featuring #Teambronwick</span></div>

<!-- team -->
<div class="abs team-head"><small>Say Hello To</small><strong><span class="accent">T</span>eambronwick</strong></div>
<p class="abs team-copy">We're a team of down to earth real estate agents who love helping people buy, sell and manage their homes. Unlike other agents we bring our full attention to each client, so you always know where things stand. We take the time to get to know you and build a plan that suits your goals.</p>
<div class="abs team-row">
  <div class="member" style="--tone:#2d3440" role="img" aria-label="Portrait photograph of a team member in a dark suit"></div>
  <div class="member" style="--tone:#4a5568" role="img" aria-label="Portrait photograph of a team member in a grey jacket"></div>
  <div class="member" style="--tone:#1f2a3a" role="img" aria-label="Portrait photograph of a team member in a navy suit"></div>
  <div class="member" style="--tone:#262626" role="img" aria-label="Portrait photograph of a team member in a black top"></div>
  <div class="member" style="--tone:#8a7a6c" role="img" aria-label="Portrait photograph of a team member in a beige blouse"></div>
  <div class="member" style="--tone:#3a3a3a" role="img" aria-label="Portrait photograph of a team member in a dark dress"></div>
  <div class="member" style="--tone:#c9c2ba" role="img" aria-label="Portrait photograph of a team member in a light top"></div>
  <div class="member" style="--tone:#2b2b30" role="img" aria-label="Portrait photograph of a team member in a black blazer"></div>
</div>
<span class="abs btn team-btn">Read More</span>

<!-- testimonials -->
<div class="abs testi-head"><small>Here's Some Kind Words</small><strong><span class="accent">F</span>rom Some Of Our<br>Raving Fans!</strong></div>
<div class="abs testi-band" role="img" aria-label="Faded photograph of a home interior behind the reviews"></div>
<svg class="abs" style="left:0;top:3270px" width="1200" height="70" viewBox="0 0 1200 70" aria-hidden="true">
  <path d="M0 30 Q600 -10 1200 40 L1200 70 L0 70Z" fill="#ef5a24"/>
  <path d="M0 50 Q600 8 1200 58 L1200 70 L0 70Z" fill="#e9e1db"/>
</svg>
<div class="quote side" style="left:-90px;padding-left:110px"><span class="qmark">“</span>We sold quickly and for more than we hoped. Friendly, honest and always available.<div class="who">— Helena Marsh</div></div>
<div class="quote main"><span class="qmark">“</span>Having dealt with a few agents over the years, this team stood out from day one. They kept us informed at every stage, gave sensible advice on presentation and found the right buyers fast. The whole process felt easy and we always knew what was happening next. Highly recommended to anyone.<div class="who">— Rob Tillard</div></div>
<div class="quote side" style="left:960px;padding-right:110px"><span class="qmark">“</span>Our rental has never been looked after so well. Quick replies and great tenants.<div class="who">— Jess Orlo</div></div>
<div class="abs pager"><i></i><i class="on"></i><i></i><i></i></div>

<!-- awards -->
<div class="abs awards-text">
  <h2><span class="accent">W</span>e're Kinda Famous!</h2>
  <p class="lead">Well not really... but we've had some really good mentions in the press (and we've won some awards along the way)</p>
  <p>As you have heard a few times, what makes us different is the care we bring to every sale and every tenancy. We keep things simple, honest and personal.</p>
  <p>We have been lucky to receive recognition from our peers and our clients, and we are proud of every result we share with them.</p>
</div>
<span class="badge gold" style="left:980px;top:3850px"></span>
<span class="badge" style="left:716px;top:3984px"></span>
<span class="badge dark sq" style="left:812px;top:3984px"></span>
<span class="badge" style="left:908px;top:3984px"></span>
<span class="badge" style="left:1004px;top:3984px"></span>
<span class="badge dark" style="left:716px;top:4088px"></span>
<span class="badge sq" style="left:812px;top:4088px"></span>
<span class="badge" style="left:908px;top:4088px"></span>
<span class="badge sq" style="left:1004px;top:4088px"></span>

<!-- contact -->
<svg class="abs contact-curve" width="1200" height="90" viewBox="0 0 1200 90" aria-hidden="true">
  <path d="M0 20 Q500 80 1200 10 L1200 26 Q500 94 0 36Z" fill="#ef5a24"/>
</svg>
<div class="abs house" role="img" aria-label="Photograph of a rendered two-storey house with a stone tower under blue sky"></div>
<div class="abs contact-text">
  <h2><span class="accent">G</span>et In Touch With Us!</h2>
  <p>Have a question about buying, selling or renting? Drop us a line below and a friendly member of our team will be in touch shortly.</p>
  <div class="form">
    <div class="field">First Name</div><div class="field">Last Name</div>
    <div class="field">Email</div><div class="field">Phone</div>
    <div class="field wide msg">Message</div>
  </div>
  <span class="btn">Submit</span>
</div>

<!-- footer -->
<footer class="abs footer"></footer>
<div class="f-item" style="left:100px">
  <svg class="f-ic" viewBox="0 0 42 42" aria-hidden="true"><circle cx="21" cy="21" r="21" fill="#ef5a24"/><path d="M21 11a7 7 0 0 0-7 7c0 5 7 13 7 13s7-8 7-13a7 7 0 0 0-7-7zm0 9.5a2.5 2.5 0 1 1 0-5 2.5 2.5 0 0 1 0 5z" fill="#fff"/></svg>
  <div><b>Address</b>Shop 1/88 Fairlie St, Wendale QLD 4190</div>
</div>
<div class="f-item" style="left:510px">
  <svg class="f-ic" viewBox="0 0 42 42" aria-hidden="true"><circle cx="21" cy="21" r="21" fill="#ef5a24"/><path d="M15 12l4 0 2 5-3 2a11 11 0 0 0 5 5l2-3 5 2 0 4c0 1-1 2-2 2-9 0-16-7-16-16 0-1 1-1 3-1z" fill="#fff"/></svg>
  <div><b>Phone No</b>0400 555 017</div>
</div>
<div class="f-item" style="left:868px">
  <svg class="f-ic" viewBox="0 0 42 42" aria-hidden="true"><circle cx="21" cy="21" r="21" fill="#ef5a24"/><rect x="11" y="14" width="20" height="14" rx="1" fill="#fff"/><path d="M11 15l10 7 10-7" stroke="#ef5a24" stroke-width="1.6" fill="none"/></svg>
  <div><b>Email</b>hello@bronwickhomes.com.au</div>
</div>
<div class="f-col" style="left:100px">
  <h4>Quick Link</h4>
  <div class="f-list">
    <span>Home</span><span>Advice</span>
    <span>About us</span><span>Finance</span>
    <span>Properties</span><span>Our Team</span>
    <span>Buy with us</span><span>Reviews</span>
    <span>Property Management</span><span>Contact</span>
  </div>
</div>
<div class="f-col" style="left:510px;width:300px">
  <h4>We're very socialised!</h4>
  <p>Make sure to follow us on our social channels for the latest listings, handy property tips, local news and a peek behind the scenes at our team. Don't forget to say hi!</p>
</div>
<div class="abs f-video" role="img" aria-label="Video thumbnail of the team walking through a listed home"></div>
<div class="abs copy">Copyright © 2019 <b>Bronwick Homes</b> Pty Ltd</div>
<div class="abs socials"><span class="dot"></span><span class="dot"></span><span class="dot"></span></div>

</body>
</html>
```